Hawaii Luxury Real Estate Sales Broker needs Stationery Design Project

I am a high end property Broker here in Hawaii. I am trying to distinguish myself and my name as a brand as opposed to just being one in hundreds of Realtors out there. I am fortunate to have positioned myself into this particular market and would like to continue to grow my business here by finding the right added touch of classy detail that will make me stand out to Buyers and Sellers of this caliber. I am looking to brand myself via stationary and ads that I can place internationally. The high net worth individuals that I will be reaching out to make this a project that needs to emulate class and sophistication but with a bit of a feminine appeal as I am a woman. :-) Because I live in Hawaii I think this too may be able to play a part of the elegance in design based on the beauty that surrounds us here in the Pacific.

Target Market(s)

High Net Worth Individuals (Calder List, Birch Rd Gazette, Private Jet owners)

Industry/Entity Type

Business

Requirements
Must have
• My initials. I would like to see my name or initials always at their fingertips as I want them to be thinking of me as their Realtor.
Should not have
• Nothing too cheesy or touristy. It is important that this is something I can confidently send to high net worth individuals.

```html
<!DOCTYPE html>
<html lang="en">
<head>
<meta charset="utf-8">
<title>Leilani Kahale – Stationery</title>
<link rel="stylesheet" href="https://fonts.googleapis.com/css2?family=Arimo:ital,wght@0,400;0,700;1,400&display=swap">
<style>
  :root {
    --page: #ffffff;
    --ink: #333333;
    --ink-soft: #777777;
    --mark: #7a7a7a;
    --band: #cfcfcf;
    --band-dark: #a9a9a9;
    --wave-light: #d4d4d4;
    --wave-mid: #bdbdbd;
    --wave-deep: #666666;
    --edge: #9a9a9a;
  }
  * { box-sizing: border-box; margin: 0; padding: 0; }
  html, body { width: 1200px; height: 900px; overflow: hidden; background: var(--page); }
  body { position: relative; font-family: "Arimo", Arial, sans-serif; color: var(--ink); }

  .sheet, .card { position: absolute; background: var(--page); overflow: hidden; }

  /* writing paper */
  .sheet { left: 72px; top: 80px; width: 574px; height: 740px; border: 1px solid #e2e2e2; }
  .sheet__top-band { position: absolute; left: 0; top: 0; width: 100%; height: 20px; background: var(--band); }
  .sheet__bottom-band { position: absolute; left: 0; bottom: 0; width: 100%; height: 16px; background: var(--band); }

  .wordmark { position: absolute; color: var(--mark); font-weight: 400; letter-spacing: 1px; text-transform: uppercase; white-space: nowrap; }
  .sheet .wordmark { right: 122px; top: 52px; font-size: 17px; line-height: 20px; text-align: right; }
  .sheet .wordmark span { display: block; }

  .contact { position: absolute; border-left: 6px solid var(--band); padding-left: 8px; font-size: 6.5px; line-height: 8.4px; color: var(--ink-soft); white-space: nowrap; }
  .contact__name { font-size: 8.5px; line-height: 10px; color: var(--ink); }
  .contact__gap { height: 8px; }
  .sheet .contact { left: 458px; top: 38px; height: 104px; }

  .wave {
    position: absolute; left: 0; bottom: 16px;
    background: radial-gradient(ellipse at 20% 100%, var(--wave-deep) 0 14%, var(--wave-mid) 15% 45%, var(--wave-light) 46% 70%, transparent 71%);
  }
  .sheet .wave { width: 540px; height: 200px; }

  /* biz cards */
  .card { left: 756px; width: 280px; height: 156px; border: 1px solid var(--edge); }
  .card--front { top: 174px; }
  .card--back { top: 370px; height: 160px; }
  .card__band { position: absolute; left: 0; bottom: 0; width: 100%; height: 8px; background: var(--band); border-top: 2px solid var(--band-dark); }
  .card .wave { bottom: 8px; width: 150px; height: 84px; }
  .card--front .wordmark { left: 120px; top: 58px; font-size: 15px; line-height: 18px; text-align: center; width: 150px; }
  .card--front .wordmark small { display: block; font-size: 7px; line-height: 10px; letter-spacing: 2px; }
  .card--back .contact { left: 170px; top: 30px; height: 88px; }

  .caption { position: absolute; font-style: italic; font-size: 17px; color: var(--ink-soft); }
  .caption--paper { left: 672px; top: 782px; }
  .caption--cards { left: 896px; top: 552px; }
</style>
</head>
<body>

<section class="sheet" aria-label="Writing paper">
  <div class="sheet__top-band"></div>
  <div class="wordmark"><span>Leilani</span><span>Kahale</span></div>
  <address class="contact">
    <div class="contact__name">Leilani Kahale</div>
    <div>Property Broker</div>
    <div>Address Line 1</div>
    <div>Address Line 2</div>
    <div class="contact__gap"></div>
    <div>Tel +00 000 000</div>
    <div>Fax +00 000 000</div>
    <div class="contact__gap"></div>
    <div>leilani@kahalehomes.com</div>
    <div>www.kahalehomes.com</div>
  </address>
  <div class="wave" role="img" aria-label="Curling grey ocean wave swirl ornament"></div>
  <div class="sheet__bottom-band"></div>
</section>

<section class="card card--front" aria-label="Business card front">
  <div class="wordmark">Kahale<small>Leilani Kahale</small></div>
  <div class="wave" role="img" aria-label="Curling grey ocean wave swirl ornament"></div>
  <div class="card__band"></div>
</section>

<section class="card card--back" aria-label="Business card back">
  <address class="contact">
    <div class="contact__name">Leilani Kahale</div>
    <div>Property Broker</div>
    <div>Address Line 1</div>
    <div>Address Line 2</div>
    <div>Tel +00 000 000</div>
    <div>Fax +00 000 000</div>
    <div>leilani@kahalehomes.com</div>
    <div>www.kahalehomes.com</div>
  </address>
  <div class="wave" role="img" aria-label="Curling grey ocean wave swirl ornament"></div>
  <div class="card__band"></div>
</section>

<p class="caption caption--cards">biz cards</p>
<p class="caption caption--paper">writing paper</p>

</body>
</html>
```